ZentaLOOM new era @ Hyper Digitalization

We need a Brochure that show all our product, services and consulting related to Hyper Digitalization into the industrial internet of things world.
We need a document that can be handled as a electronic brochure, this means that we need to show strong corporate presence, with strong skill of technology, and we have credentials and key sucess projects related to Manufacturing industries.
Key industries that we attend: Automotive, Chemical, Food and Beverage, Mining, Paper and Pulp, Oil and Gas, Energy Management.
We save money to our customer in 6 ways: 1) Eficiency in operation 2) Production Control 3) Hyper Digitalization of Thing Optimizing asset ussage 4) Maintenance and predictive of assets risks 5) Quality Control reducing Cost 6) Augmented Reality in operation and control
Target Market(s)
Manufacturing Industry. CEO of companies that has challenges of saving operation costs into plants of manufacturing.
Industry/Entity Type
Software
Font styles to use
Other font styles liked:
- MONTSERRAT
Requirements
Must have
- Technology Enviroment, our logo, our expertise, simple message about what our company does and the DNA, infography of the company, cases of sucess, cases of savings $ using our tecnology and services, what we can do for the customer in a few words
Nice to have
- standarize our colors related to our presentation, futuristic, information related to Artificial Inteligence related to machinery
Should not have
- old version of technology,

```html
<!DOCTYPE html>
<html lang="es">
<head>
<meta charset="utf-8">
<title>ZentaLOOM 2021 – Hyper Digitalization</title>
<link href="https://fonts.googleapis.com/css2?family=Montserrat:wght@300;400;500;600;700;800&display=swap" rel="stylesheet">
<style>
  :root{
    --navy:#0b3352;
    --blue:#0a78bf;
    --bright:#1e98e3;
    --grey:#8c9196;
    --ink:#2b2b2b;
    --stage:#e4e4e4;
    --line:#c9ccd0;
  }
  *{margin:0;padding:0;box-sizing:border-box}
  html,body{width:1200px;height:3000px;overflow:hidden;background:var(--stage);font-family:'Montserrat',sans-serif;color:var(--ink)}
  .brochure{position:relative;width:1200px;height:3000px}
  .page{position:absolute;left:231px;width:728px;height:515px;background:#fff;box-shadow:0 4px 10px rgba(0,0,0,.18);overflow:hidden}
  .page--cover{top:89px;background:var(--navy)}
  .page--intro{top:669px}
  .page--quote{top:1248px}
  .page--detail{top:1840px}
  .page--back{top:2429px}

  /* cover */
  .cover-art{position:absolute;inset:0;width:728px;height:515px}
  .cover-title{position:absolute;left:51px;top:198px;color:#fff;font-weight:700;font-size:40px;letter-spacing:1px;line-height:1}
  .cover-year{position:absolute;left:51px;top:246px;color:#fff;font-weight:300;font-size:38px;line-height:1}
  .cover-rule{position:absolute;left:51px;top:315px;width:285px;height:1px;background:#9fb3c4}
  .cover-rule::before{content:"";position:absolute;left:22px;top:-3px;width:48px;height:6px;border-radius:3px;background:var(--bright)}
  .cover-tag{position:absolute;left:51px;top:356px;color:#fff;font-weight:700;font-size:21px;letter-spacing:.5px}
  .cover-tag span{color:var(--bright);font-weight:400}
  .cover-web{position:absolute;left:51px;top:449px;color:#d6e0ea;font-weight:300;font-size:19px}
  .cover-brand{position:absolute;left:421px;top:440px;font-size:36px;font-weight:600;color:var(--blue);letter-spacing:.5px}

  /* shared */
  .brand{font-weight:600;color:var(--blue);letter-spacing:.5px}
  .footer{position:absolute;left:0;top:0;width:728px;height:515px;pointer-events:none}
  .footer-brand{position:absolute;left:36px;top:440px;font-size:28px;line-height:1.2}
  .footer-rule{position:absolute;left:222px;top:452px;width:450px;height:1px;background:var(--line)}
  .footer-web{position:absolute;left:466px;top:452px;width:214px;height:27px;background:var(--navy);clip-path:polygon(14px 0,100% 0,100% 100%,0 100%);color:#fff;font-weight:300;font-size:16px;line-height:27px;padding-left:24px}
  .footer-num{position:absolute;left:664px;top:452px;width:28px;height:28px;border-radius:50%;background:#fff;border:1.5px solid var(--navy);color:var(--navy);font-size:15px;text-align:center;line-height:25px}

  .photo{position:absolute;border:3px solid #fff;box-shadow:0 1px 5px rgba(0,0,0,.3)}
  .body-copy{font-size:10.4px;line-height:1.18;text-align:justify}
  .body-copy p+p{margin-top:12px}
  .body-copy b{font-weight:600}

  /* intro */
  .intro-bar{position:absolute;left:0;top:65px;width:22px;height:50px;background:var(--navy)}
  .intro-title{position:absolute;left:36px;top:58px;color:var(--blue);font-weight:800;font-size:30px;letter-spacing:.3px;line-height:1.2}
  .intro-sub{position:absolute;left:36px;top:95px;font-size:24px;font-weight:400;color:#222;line-height:1.2}
  .intro-copy{position:absolute;left:36px;top:161px;width:356px}
  .intro-photo{left:429px;top:161px;width:256px;height:233px;background:radial-gradient(circle at 55% 38%,#8a6a3a 0,#2c3542 22%,#14181e 60%,#0b0d11 100%)}

  /* quote */
  .quote-photo{position:absolute;left:0;top:61px;width:446px;height:341px;background:linear-gradient(180deg,#eef1f4 0%,#c9cfd6 45%,#3a4250 75%,#8d939b 100%);box-shadow:0 1px 5px rgba(0,0,0,.3)}
  .quote-box{position:absolute;left:406px;top:101px;width:278px;height:265px;background:var(--blue);color:#fff;padding:34px 28px 0 29px;font-size:10.4px;line-height:1.2}
  .quote-box p+p,.quote-box p+ol,.quote-box ol+p{margin-top:10px}
  .savings{list-style:none;counter-reset:way}
  .savings li{counter-increment:way;padding-left:14px;position:relative}
  .savings li::before{content:counter(way) ")";position:absolute;left:0;font-weight:600}

  /* detail */
  .detail-title{position:absolute;left:38px;top:96px;color:var(--grey);font-weight:700;font-size:19px;letter-spacing:.3px;line-height:1.2}
  .detail-copy{position:absolute;left:38px;top:140px;width:320px}
  .detail-band{position:absolute;left:657px;top:104px;width:71px;height:311px;background:var(--blue)}
  .detail-photo-a{left:399px;top:138px;width:288px;height:114px;background:radial-gradient(ellipse at 50% 45%,#9fb8cf 0,#2f5d86 25%,#0f2a44 65%,#0a1a2b 100%)}
  .detail-photo-b{left:399px;top:274px;width:288px;height:114px;background:radial-gradient(ellipse at 35% 30%,#7fc6f2 0,#3b6c98 30%,#1a2f4b 70%,#101e33 100%)}

  /* back */
  .back-pattern{position:absolute;left:0;top:0;width:728px;height:375px;background:radial-gradient(ellipse at 85% 35%,#e9ebee 0,#f4f5f6 45%,#fff 80%)}
  .back-brand{position:absolute;left:0;width:728px;top:310px;text-align:center;font-size:36px;line-height:1.2}
  .back-band{position:absolute;left:0;top:375px;width:728px;height:140px}
  .contact{position:absolute;left:0;width:728px;top:388px;text-align:center;color:#fff;font-weight:300;font-size:19px;line-height:27px}
  .contact li{list-style:none;display:flex;align-items:center;justify-content:center;gap:6px}
  .contact svg{width:12px;height:12px}
  .social{display:flex;justify-content:center;gap:5px;margin-top:6px}
  .social i{display:block;width:9px;height:9px;border-radius:50%}
</style>
</head>
<body>
<main class="brochure">

  <!-- Cover -->
  <section class="page page--cover">
    <svg class="cover-art" viewBox="0 0 625 442" preserveAspectRatio="none">
      <defs>
        <radialGradient id="globeTone" cx="70%" cy="38%" r="60%">
          <stop offset="0" stop-color="#3a8fd0"/>
          <stop offset=".45" stop-color="#12457a"/>
          <stop offset="1" stop-color="#061a30"/>
        </radialGradient>
      </defs>
      <polygon points="212,0 625,0 625,398" fill="url(#globeTone)" role="img" aria-label="Globo digital de red en tonos azules"/>
      <polygon points="178,0 212,0 625,398 625,420" fill="#1e98e3"/>
      <polygon points="158,0 168,0 470,292 462,296" fill="#ffffff"/>
      <polygon points="255,442 470,290 625,432 625,442" fill="#ffffff"/>
      <polygon points="470,290 478,285 625,418 625,432" fill="#1e98e3"/>
    </svg>
    <h1 class="cover-title">ZENTALOOM</h1>
    <div class="cover-year">2021</div>
    <div class="cover-rule"></div>
    <div class="cover-tag">HYPER <span>DIGITALIZATION</span></div>
    <div class="cover-web">www.zentaloom.com</div>
    <div class="cover-brand">ZentaLOOM</div>
  </section>

  <!-- Page 2: who we are -->
  <section class="page page--intro">
    <div class="intro-bar"></div>
    <h2 class="intro-title">HIPERDIGITALIZACIÓN</h2>
    <div class="intro-sub">la nueva era de la industria</div>
    <div class="intro-copy body-copy">
      <p>ZentaLOOM desarrolla software de hiperdigitalización para el internet industrial de las cosas: conectamos máquinas, datos y personas para que cada planta de manufactura opere con menos costo y más control.</p>
      <p>Nuestro ADN es la tecnología aplicada: inteligencia artificial sobre maquinaria, analítica en tiempo real y realidad aumentada en la operación.</p>
      <p>Atendemos Automotriz, Química, Alimentos y Bebidas, Minería, Papel y Celulosa, Petróleo y Gas y Gestión de Energía.</p>
      <p>Ofrecemos productos, servicios y consultoría para directores que buscan reducir los costos de operación de sus plantas.</p>
      <p>En pocas palabras: convertimos cada activo en un dato útil y cada dato en un ahorro medible, con proyectos de éxito en las principales industrias de manufactura.</p>
    </div>
    <div class="photo intro-photo" role="img" aria-label="Ejecutivo sosteniendo una bombilla con red digital luminosa"></div>
    <div class="footer">
      <div class="footer-rule"></div>
      <div class="footer-brand brand">ZentaLOOM</div>
      <div class="footer-web">www.zentaloom.com</div>
      <div class="footer-num">2</div>
    </div>
  </section>

  <!-- Page 3: six ways to save -->
  <section class="page page--quote">
    <div class="quote-photo" role="img" aria-label="Equipo de ejecutivos estrechando las manos en una oficina luminosa"></div>
    <div class="quote-box">
      <p>Ahorramos dinero a nuestros clientes de seis maneras:</p>
      <ol class="savings">
        <li>Eficiencia en la operación.</li>
        <li>Control de la producción.</li>
        <li>Hiperdigitalización de las cosas, optimizando el uso de activos.</li>
        <li>Mantenimiento y predicción de riesgos de los activos.</li>
        <li>Control de calidad que reduce costos.</li>
        <li>Realidad aumentada en operación y control.</li>
      </ol>
      <p>Con inteligencia artificial sobre la maquinaria, cada planta alcanza mayor productividad con lo que ya tiene.</p>
    </div>
    <div class="footer">
      <div class="footer-rule"></div>
      <div class="footer-brand brand">ZentaLOOM</div>
      <div class="footer-web">www.zentaloom.com</div>
      <div class="footer-num">3</div>
    </div>
  </section>

  <!-- Page 4: success cases -->
  <section class="page page--detail">
    <h2 class="detail-title">CASOS DE ÉXITO</h2>
    <div class="detail-copy body-copy">
      <p><b>Automotriz:</b> una planta de ensamble conectó 240 equipos a nuestra plataforma. La eficiencia general subió 18% y el ahorro anual superó $1.2 millones de dólares gracias al control de producción en tiempo real.</p>
      <p><b>Minería:</b> el mantenimiento predictivo con inteligencia artificial redujo 35% los paros no programados de la flota.</p>
      <p><b>Alimentos y Bebidas:</b> el control de calidad automatizado bajó 22% la merma y ahorró $480 mil dólares al año; la realidad aumentada redujo a la mitad la capacitación.</p>
      <p>ZentaLOOM suma 15 años de existencia y más de 120 proyectos de hiperdigitalización en siete industrias clave.</p>
    </div>
    <div class="detail-band"></div>
    <div class="photo detail-photo-a" role="img" aria-label="Manos señalando un globo digital brillante"></div>
    <div class="photo detail-photo-b" role="img" aria-label="Apretón de manos sobre una ciudad iluminada"></div>
    <div class="footer">
      <div class="footer-rule"></div>
      <div class="footer-brand brand">ZentaLOOM</div>
      <div class="footer-web">www.zentaloom.com</div>
      <div class="footer-num">4</div>
    </div>
  </section>

  <!-- Back cover -->
  <section class="page page--back">
    <div class="back-pattern" role="img" aria-label="Red tenue de nodos conectados en gris claro"></div>
    <div class="back-brand brand">ZentaLOOM</div>
    <svg class="back-band" viewBox="0 0 728 140" preserveAspectRatio="none">
      <rect width="728" height="140" fill="#0b3352"/>
      <polygon points="0,4 0,140 92,140" fill="#0a78bf"/>
      <polygon points="0,0 6,0 98,140 92,140" fill="#ffffff"/>
    </svg>
    <ul class="contact">
      <li><svg viewBox="0 0 12 12"><path d="M3 1l2 2.5-1.2 1.2a6 6 0 0 0 3.5 3.5L8.5 7 11 9l-1 2C5 11 1 7 1 2z" fill="#1e98e3"/></svg>010.555.0147</li>
      <li><svg viewBox="0 0 12 12"><rect x="1" y="3" width="10" height="7" fill="#1e98e3"/><path d="M1 3l5 4 5-4" stroke="#0b3352" fill="none"/></svg>hello@zentaloom.com</li>
      <li><svg viewBox="0 0 12 12"><circle cx="6" cy="6" r="5" fill="#1e98e3"/><path d="M1 6h10M6 1c-3 3-3 7 0 10M6 1c3 3 3 7 0 10" stroke="#0b3352" fill="none" stroke-width=".8"/></svg>www.zentaloom.com</li>
      <li class="social"><i style="background:#e2568c"></i><i style="background:#3f6db3"></i><i style="background:#1e98e3"></i></li>
    </ul>
  </section>

</main>
</body>
</html>
```